Realtor Website Design

We are working with KRV•DEL. They are a financial advising company that needs a new website design.

Some sites to use for inspiration:

https://www.morvathine.com
https://www.pildovanhomes.com

Thank you for taking the time to consider designing a website for us. We are web developers based in Stockton and Los Angeles, CA, USA. Most of our projects go through the same process. Understanding this process may help you win a project with us. We custom-code all of our websites in-house. We don’t have any requirements as to what tools you use for your design, but we prefer Figma files. For any design that we label as four-stars, we send it to the client for review. The client picks the final design they want us to use. Once we complete this process, we will continue to show additional clients all the four-star sites and purchase them later. Your designs will have multiple chances to sell. For better chances of success, we ask that you follow these guidelines.

IMAGES:
If you use any images or icons in the design, we ask that you have a link to the asset so we can purchase the image/icon. Most of the designs we submit do not have the customer’s images on them unless they have some great images. Be creative; show us the feeling you are trying to portray with your image choices. Use any royalty-free site you choose. We subscribe to Zentiq and mainly use their images, but we can purchase images outside of Zentiq.

PLEASE NOTE: we will not submit designs to clients with watermarks on the images.

FONTS:
We ask that you identify the fonts used in the design. This can be done in a message if you want. We typically use Google Fonts and Zentiq Fonts.

CONTENT:
We're always open to different content and ideas. We often submit designs with stock images so the client can see our vision. We typically take pictures after the website launch to use their images with our vision. Lorem Ipsum is fine for paragraphs, but we ask that you write the headers in correct English. We want to be able to show the vision and identify the sections of the website.

INSPIRATION:
We typically add a couple of links in the brief of websites we like to help you get started in your design.

REVISIONS:
We do not often ask for revisions of the designs unless we see something in the design that may not appeal to the client. If there are slight changes that we want to make, we do that in the development process.

FEEDBACK:
We rarely give feedback on designs during the design process. We are working on many website projects and do not have the time to provide feedback. We usually respond if your request is well thought out and asks specific questions, but a note asking “feedback, please” usually goes unanswered.

```html
<!DOCTYPE html>
<html lang="en">
<head>
<meta charset="utf-8">
<title>Larkfield Realty</title>
<link href="https://fonts.googleapis.com/css2?family=Poppins:ital,wght@0,300;0,400;0,500;0,600;1,400&display=swap" rel="stylesheet">
<style>
:root{
  --teal:#3f998e;
  --teal-dark:#2f7d73;
  --teal-light:#8fcdc1;
  --ink:#1e1e1e;
  --text:#3a3a3a;
  --muted:#8a8a8a;
  --line:#c9d9d6;
  --cream:#f8f6f3;
  --white:#ffffff;
}
*{margin:0;padding:0;box-sizing:border-box}
html,body{width:1200px;height:4938px;overflow:hidden}
body{font-family:"Poppins",sans-serif;color:var(--text);background:var(--white);position:relative}
.abs{position:absolute}
section,header,footer{position:absolute;left:0;width:1200px}
.btn{position:absolute;background:var(--teal);color:var(--white);display:flex;align-items:center;justify-content:center;font-weight:400}
.heading{position:absolute;font-weight:400;color:var(--ink);letter-spacing:1px;line-height:1}
.rule{position:absolute;height:1px;background:var(--teal-light)}
.para{position:absolute;font-size:13px;line-height:25.5px;color:var(--text);text-align:justify}

/* header */
.site-header{top:0;height:128px;background:var(--white)}
.brand{position:absolute;font-weight:500;color:var(--teal);font-size:26px;letter-spacing:1px;white-space:nowrap}
.nav{position:absolute;top:48px;left:536px;display:flex;font-size:13px;color:var(--ink)}
.nav a{text-decoration:none;color:inherit;margin-right:36px}
.nav a.active{color:var(--teal)}
.nav-contact{left:1040px;top:40px;width:96px;height:34px;font-size:13px}

/* hero */
.hero{top:128px;height:728px;background:linear-gradient(135deg,#cfc6bb 0%,#9e8f80 45%,#6d5f55 100%)}
.hero-text{position:absolute;left:0;width:1200px;text-align:center;color:var(--white)}

/* about */
.about-photo{left:60px;top:1110px;width:520px;height:200px;background:linear-gradient(90deg,#b9a488,#e6ded2 50%,#a89378);border-radius:100px}

/* services */
.card{position:absolute;top:1895px;width:330px;height:443px;background:var(--white);box-shadow:0 2px 10px rgba(0,0,0,.15)}
.card-photo{position:absolute;left:12px;top:12px;width:306px;height:225px;background:linear-gradient(135deg,#6f7f77,#c9cfcb 55%,#3f4a49);clip-path:polygon(0 0,100% 0,100% 87%,50% 100%,0 87%)}
.card h3{position:absolute;top:233px;left:0;width:100%;text-align:center;font-size:22px;font-weight:500;color:var(--teal)}
.card h3::after{content:"";display:block;width:40px;height:2px;background:var(--teal);margin:6px auto 0}
.card p{position:absolute;top:275px;left:25px;width:280px;text-align:center;font-size:13px;line-height:24px}
.card .btn{left:106px;top:362px;width:118px;height:44px;font-size:11px;font-weight:500}

/* band */
.band{top:2460px;height:487px;background:linear-gradient(135deg,#3b3a38,#5c554e 50%,#2e2d2c)}

/* reviews */
.reviews{top:2947px;height:660px;background:var(--cream)}
.review{position:absolute;top:293px;width:464px;height:225px;border:1.5px solid #d9d9d9;border-radius:28px;background:var(--white)}
.quote{position:absolute;top:-42px;left:60px;font-size:96px;line-height:1;color:var(--teal-light);font-family:Georgia,serif;background:var(--white);padding:0 8px}
.stars{position:absolute;top:52px;right:30px;color:#f0b400;font-size:15px;letter-spacing:1px}
.review p{position:absolute;top:90px;left:36px;width:400px;font-size:11.5px;line-height:21px;font-style:italic;color:#555}
.person{position:absolute;top:543px;display:flex;align-items:center;gap:14px}
.avatar{width:66px;height:66px;border-radius:50%;background:linear-gradient(135deg,#d6cbbf,#7b6e63)}
.person b{display:block;font-size:13px;font-weight:600;color:var(--ink)}
.person span{font-size:11px;color:var(--muted)}
.arrow{position:absolute;top:372px;width:46px;height:46px;border-radius:50%;display:flex;align-items:center;justify-content:center}
.dots{position:absolute;top:622px;left:562px;display:flex;gap:14px}
.dots i{width:8px;height:8px;border-radius:50%;border:1.5px solid var(--teal)}
.dots i.on{background:var(--teal)}

/* contact */
.field{position:absolute;border:1px solid #dcdcdc;background:var(--white);font-size:11px;color:var(--muted);padding:12px 16px}
.contact-photo{left:660px;top:3808px;width:485px;height:452px;background:linear-gradient(135deg,#8d7866,#d9c9b6 45%,#4f5b5d);clip-path:polygon(2% 0,100% 0,65% 100%,0 100%,0 3%);border-radius:14px}
.contact-accent{left:660px;top:3808px;width:485px;height:452px;background:var(--teal);clip-path:polygon(93% 0,100% 3%,71% 100%,63% 100%)}

/* partners */
.partner{position:absolute;top:4430px;width:208px;height:120px;background:var(--white);box-shadow:0 2px 10px rgba(0,0,0,.1);display:flex;align-items:center;justify-content:center}
.partner span{display:block;width:110px;height:60px;background:#e6e9ea;border-radius:4px}

/* footer */
.site-footer{top:4630px;height:308px;background:#44998e;color:var(--white)}
.col{position:absolute;top:35px;border-left:2px solid rgba(255,255,255,.9);height:165px;padding-left:24px}
.col h4{font-size:14px;font-weight:400;letter-spacing:.5px;margin-top:8px}
.col li{list-style:none;font-size:11px;margin-top:10px}
.col li::before{content:"";display:inline-block;width:20px;height:1px;background:var(--white);vertical-align:middle;margin-right:8px}
.info{display:flex;gap:12px;margin-top:14px;font-size:11px;line-height:13px}
.ico{width:22px;height:22px;border:1px solid var(--white);border-radius:3px;flex:none;display:flex;align-items:center;justify-content:center}
.social{position:absolute;top:175px;display:flex;gap:6px}
.social i{width:22px;height:22px;background:var(--white);border-radius:3px}
</style>
</head>
<body>

<header class="site-header">
  <div class="brand" style="left:70px;top:42px">Larkfield Realty</div>
  <nav class="nav">
    <a class="active">Home</a><a>About</a><a>Listings</a><a>Reviews</a><a>Portfolio</a><a>Resources</a>
  </nav>
  <div class="btn nav-contact">Contact</div>
</header>

<section class="hero" role="img" aria-label="Photo of a handshake over a desk with a small model house and paperwork">
  <div class="hero-text" style="top:272px;font-size:24px">Welcome To</div>
  <div class="hero-text" style="top:330px;font-size:64px;font-weight:500;letter-spacing:2px">Larkfield Realty</div>
  <div class="hero-text" style="top:533px;font-size:22px;font-weight:300">Lorem ipsum dolor sit amet, consectetur adipiscing</div>
  <div class="btn" style="left:460px;top:612px;width:240px;height:56px;font-size:28px">Contact Us</div>
</section>

<section style="top:856px;height:900px">
  <h2 class="heading" style="left:636px;top:190px;font-size:54px">ABOUT US</h2>
  <div class="rule" style="left:488px;top:254px;width:422px"></div>
</section>
<div class="abs about-photo" role="img" aria-label="Bright interior photo of a modern living space in a roof-shaped frame"></div>
<p class="para" style="left:636px;top:1135px;width:462px">Lorem ipsum dolor sit amet, consectetur adipiscing elit, sed do eiusm od tempor incididunt ut labore et dolore magna aliqua. Quis ipsum suspendisse ultrices gravida. Risus commodo viverra maecenas acc umsan lacus vel facilisis. Lorem ipsum dolor sit amet, consectetur adipiscing elit, sed do eiusmod tempor incididunt ut labore et dolore magna aliqua. Lorem ipsum dolor sit amet, consectetur adipiscing elit, sed do eiusmod tempor incididunt ut labore et dolore magna aliqua. Quis ipsum suspendisse ultrices gravida. Risus commodo viverra maecenas accumsan lacus vel facilisis. Lorem ipsum dolor sit amet, consectetur adipiscing elit, sed do eiusmod tempor incididunt ut labore et dolore magna aliqua.</p>
<div class="btn" style="left:640px;top:1465px;width:180px;height:47px;font-size:24px">Contact Us</div>

<h2 class="heading" style="left:0;width:1200px;text-align:center;top:1728px;font-size:54px">SERVICES OFFERED</h2>
<div class="rule" style="left:700px;top:1790px;width:438px"></div>

<div class="card" style="left:85px"><div class="card-photo" role="img" aria-label="Office photo of business people shaking hands"></div><h3>Service 1</h3><p>Lorem ipsum dolor sit amet, consectetur adipiscing elit, sed do eiusmod tempor incididunt ut labore et dolore magna</p><div class="btn">READ MORE</div></div>
<div class="card" style="left:446px"><div class="card-photo" role="img" aria-label="Office photo of two advisors reviewing documents"></div><h3>Service 2</h3><p>Lorem ipsum dolor sit amet, consectetur adipiscing elit, sed do eiusmod tempor incididunt ut labore et dolore magna</p><div class="btn">READ MORE</div></div>
<div class="card" style="left:806px"><div class="card-photo" role="img" aria-label="Office photo of business people shaking hands"></div><h3>Service 3</h3><p>Lorem ipsum dolor sit amet, consectetur adipiscing elit, sed do eiusmod tempor incididunt ut labore et dolore magna</p><div class="btn">READ MORE</div></div>

<section class="band" role="img" aria-label="Dark photo of hands holding a model house beside stacks of coins">
  <h2 class="hero-text" style="top:122px;font-size:36px;font-weight:500;letter-spacing:.5px">EXPERT STRATEGIES FOR SERIOUS INVESTORS</h2>
  <p class="hero-text" style="top:208px;font-size:16px;line-height:25px">Lorem ipsum dolor sit amet, conse ctetur adipiscing elit, sed do eiu smod tempor incididunt ut<br>labore et dolore magna aliqua. Quis ipsum suspendisse ultrices gravida.</p>
  <div class="btn" style="left:433px;top:325px;width:287px;height:65px;font-size:34px">Contact Us</div>
</section>

<section class="reviews">
  <h2 class="heading" style="left:0;width:1200px;text-align:center;top:105px;font-size:54px">CUSTOMER REVIEWS</h2>
  <div class="rule" style="left:65px;top:181px;width:543px"></div>
  <div class="arrow" style="left:10px;background:var(--white)"><svg width="12" height="12" viewBox="0 0 12 12"><path d="M8 1 3 6l5 5" fill="none" stroke="#333" stroke-width="1.6"/></svg></div>
  <div class="arrow" style="left:1135px;background:var(--teal)"><svg width="12" height="12" viewBox="0 0 12 12"><path d="M4 1l5 5-5 5" fill="none" stroke="#fff" stroke-width="1.6"/></svg></div>
  <div class="review" style="left:113px"><div class="quote">“</div><div class="stars">★★★★★</div><p>Lorem ipsum dolor sit amet, consectetur adipiscing elit, sed do e iusmod tempor incididunt ut labore et dolore magna aliqua. Ut enim ad minim veniam, quis nostrud exercitation ullamco laboris nisi ut aliquip ex ea commodo consequat.</p></div>
  <div class="review" style="left:622px"><div class="quote">“</div><div class="stars">★★★★★</div><p>Lorem ipsum dolor sit amet, consectetur adipiscing elit, sed do eiusmod tempor incididunt ut labore et dolore magna aliqua. Ut enim ad minim veniam, quis nostrud exercitation ullamco laboris nisi ut aliquip ex ea commodo consequat. Duis aute irure dolor in reprehenderit in voluptate velit.</p></div>
  <div class="person" style="left:220px"><div class="avatar" role="img" aria-label="Portrait photo of the reviewer"></div><div><b>DARREN COLBY</b><span>Lorem ipsum</span></div></div>
  <div class="person" style="left:730px"><div class="avatar" role="img" aria-label="Portrait photo of the reviewer"></div><div><b>MARCUS ELWIN</b><span>Lorem ipsum</span></div></div>
  <div class="dots"><i class="on"></i><i></i><i></i><i></i></div>
</section>

<h2 class="heading" style="left:125px;top:3808px;font-size:54px">CONTACT US</h2>
<div class="rule" style="left:125px;top:3866px;width:535px"></div>
<p class="abs" style="left:128px;top:3880px;font-size:16px;line-height:26px;color:var(--text)">Lorem ipsum dolor sit amet, consectetur adipiscing<br>elit, sed do eiusmod tempor incididunt ut labore et</p>
<div class="field" style="left:123px;top:3992px;width:200px;height:38px">First Name:</div>
<div class="field" style="left:340px;top:3992px;width:200px;height:38px">Last Name:</div>
<div class="field" style="left:123px;top:4050px;width:200px;height:38px">Phone:</div>
<div class="field" style="left:340px;top:4050px;width:200px;height:38px">Email:</div>
<div class="field" style="left:123px;top:4110px;width:417px;height:128px">Message:</div>
<div class="btn" style="left:125px;top:4250px;width:160px;height:42px;font-size:20px">SUBMIT</div>
<div class="abs contact-accent"></div>
<div class="abs contact-photo" role="img" aria-label="Photo of a smiling couple reviewing paperwork on a tablet"></div>

<div class="partner" style="left:62px" role="img" aria-label="Partner badge"><span></span></div>
<div class="partner" style="left:318px" role="img" aria-label="Partner badge"><span></span></div>
<div class="partner" style="left:573px" role="img" aria-label="Partner badge"><span></span></div>
<div class="partner" style="left:827px" role="img" aria-label="Partner badge"><span></span></div>

<footer class="site-footer">
  <div class="brand" style="left:100px;top:100px;color:var(--white);font-size:24px">Larkfield Realty</div>
  <div class="social" style="left:146px"><i></i><i></i><i></i><i></i></div>
  <div class="col" style="left:410px"><h4>QUICK LINKS</h4><ul><li>Home</li><li>About Us</li><li>Listings</li><li>Reviews</li><li>Contact</li></ul></div>
  <div class="col" style="left:600px"><h4>CONTACT US</h4>
    <div class="info"><span class="ico"><svg width="11" height="11" viewBox="0 0 12 12"><path d="M2 1h3l1 3-2 1a7 7 0 0 0 3 3l1-2 3 1v3c-6 1-10-4-9-9z" fill="none" stroke="#fff"/></svg></span><span>CALL US<br>8012 555 0142</span></div>
    <div class="info"><span class="ico"><svg width="11" height="9" viewBox="0 0 12 9"><rect x=".5" y=".5" width="11" height="8" fill="none" stroke="#fff"/><path d="M.5.5 6 5l5.5-4.5" fill="none" stroke="#fff"/></svg></span><span>EMAIL US<br>info@larkfieldrealty.com</span></div>
    <div class="info"><span class="ico"><svg width="9" height="12" viewBox="0 0 10 13"><path d="M5 12S1 7 1 5a4 4 0 0 1 8 0c0 2-4 7-4 7z" fill="none" stroke="#fff"/><circle cx="5" cy="5" r="1.4" fill="#fff"/></svg></span><span>Address line Dummy Here<br>Address line Here</span></div>
  </div>
  <div class="col" style="left:868px;width:260px"><h4>NEWSLETTER SIGN UP</h4>
    <p style="font-size:11px;line-height:14px;margin-top:26px">Subscribe our newsletter to get<br>the latest news.</p>
    <div style="margin-top:14px;width:186px;height:30px;border:1px solid var(--white);border-radius:15px;font-size:9px;padding:9px 14px;position:relative">Enter Email Address<span style="position:absolute;right:5px;top:4px;width:20px;height:20px;border:1px solid #fff;border-radius:50%;display:flex;align-items:center;justify-content:center"><svg width="10" height="8" viewBox="0 0 10 8"><path d="M0 4h9M6 1l3 3-3 3" fill="none" stroke="#fff"/></svg></span></div>
  </div>
  <div style="position:absolute;left:72px;top:266px;width:1056px;height:1px;background:rgba(255,255,255,.8)"></div>
  <p style="position:absolute;top:280px;width:1200px;text-align:center;font-size:10px">Copyright © 2024 All Rights Reserved By Company name</p>
</footer>

</body>
</html>
```